Menu Design Project for New Catering company

I would like to see my menus in a warm, inviting format. I prepare food for small intimate dinners, business lunches, picnics, parties, weddings and rehearsal dinners. I work with clients to help create their dream whether it includes items on my menu or to prepare very personal dishes that bring them warm memories of a special time or moment.

Target Market(s)

Organizations, wedding and or event planners

Industry/Entity Type

Catering

Requirements
Must have
• I would like to include the logo that is included in the attachment below. I also included a copy of the poster Lex Doyle created for me. I hope this helps. Please be creative. I am a very happy, cheerful person that enjoys cooking and having fun. I would like the design to represent my personality as well as my food. When I cater I treat my customers like an extension of my family and it comes across to them with everything I do for them. I hope this can somehow be reflected in your designs.
Should not have
• I'm open to all ideas and don't want to limit your creativity.

```html
<!DOCTYPE html>
<html lang="en">
<head>
<meta charset="utf-8">
<title>Catering Menu</title>
<link href="https://fonts.googleapis.com/css2?family=Lobster&family=Source+Sans+3:wght@600;700&display=swap" rel="stylesheet">
<style>
:root{
  --green:#2f9a3c;
  --border:#6bb36f;
  --brown:#5a3318;
  --ink:#1c1c1c;
  --paper:#ffffff;
}
*{box-sizing:border-box;margin:0;padding:0}
html,body{width:776px;height:1200px;overflow:hidden;background:var(--paper)}
body{position:relative;font-family:"Source Sans 3",Arial,sans-serif;font-weight:700;color:var(--ink);font-size:15.5px;line-height:1.32}
.section{position:absolute;left:24px;width:546px;border:1.5px solid var(--border);padding:22px 16px 12px}
.section-title{position:absolute;top:-24px;left:50%;transform:translateX(-50%);background:var(--paper);padding:0 12px;font-family:"Lobster",cursive;font-weight:400;font-size:31px;color:var(--brown);line-height:1.4;white-space:nowrap}
.salads{top:36px;height:302px;padding-top:14px}
.sides{top:380px;height:236px}
.desserts{top:645px;height:100px}
.appetizers{top:782px;height:233px}
.drinks{top:1047px;height:140px}
.salad-name{color:var(--green);margin-top:10px}
.salad-name:first-child{margin-top:0}
.cols{display:grid;grid-template-columns:1fr 1fr;column-gap:14px}
.cols p{margin-bottom:4px}
.desserts .cols{grid-template-columns:248px 1fr}
.price-note{color:var(--green);margin-bottom:6px}
.price-row{display:flex;justify-content:space-between;margin-bottom:5px}
.price-row .price{color:var(--green);white-space:nowrap;padding-left:12px}
.photo{position:absolute;left:580px;width:196px}
.photo-pastries{top:0;height:360px;background:linear-gradient(160deg,#6b5139,#3a2a1e 60%,#1e1814)}
.photo-cupcakes{top:367px;height:350px;background:linear-gradient(170deg,#e6e2dc,#c9a98a 55%,#a98866)}
.photo-buffet{top:726px;height:474px;background:linear-gradient(175deg,#c6a88a,#7a4a3a 45%,#8c2a2a 75%,#5c1a1c)}
</style>
</head>
<body>

<section class="section salads">
  <h2 class="section-title">Salads</h2>
  <p class="salad-name">Chopped Salad</p>
  <p>Lettuce, Cinnamon Candied Pecans, Green Onions, Celery, Blue Cheese Vinaigrette and Blue Cheese Crumbles</p>
  <p class="salad-name">Spinach Salad</p>
  <p>Fresh Spinach, Red Onions, Candied Pecans and Strawberries (when strawberries are available and/or in season)</p>
  <p class="salad-name">House Salad</p>
  <p>Mixed Greens, Tomatoes, Carrots, Cucumbers, Croutons and Choice of two types of Dressing (Ranch, Honey Mustard, Italian, or Blue Cheese)</p>
</section>

<section class="section sides">
  <h2 class="section-title">Other Sides</h2>
  <div class="cols">
    <div>
      <p>Broccoli Casserole</p>
      <p>Garlic Roasted Broccoli and Carrots</p>
      <p>Honey Glazed Carrots</p>
      <p>Macaroni Salad</p>
      <p>Old Fashioned Green Beans</p>
      <p>Pasta Salad</p>
      <p>Potato Salad</p>
    </div>
    <div>
      <p>Potatoes – Garlic Mashed, Scalloped, or Baked</p>
      <p>Southern Baked Beans</p>
      <p>Stewed Tomatoes</p>
      <p>Sweet &amp; Sour Slaw</p>
      <p>Sweet Corn (Creamed, Skillet Fried or Corn on the Cob)</p>
      <p>Sweet Potato Casserole</p>
    </div>
  </div>
</section>

<section class="section desserts">
  <h2 class="section-title">Desserts</h2>
  <div class="cols">
    <div><p>Cheesecakes</p><p>Cream Pies</p><p>Cupcakes</p></div>
    <div><p>Fruit Pies</p><p>Key Lime Pie</p></div>
  </div>
</section>

<section class="section appetizers">
  <h2 class="section-title">Appetizers</h2>
  <p class="price-note">Priced per appetizer/per person</p>
  <div class="price-row"><span>Sweet and Spicy Meatballs</span><span class="price">$3.00/person</span></div>
  <div class="price-row"><span>Pinwheels (various) with salsas and/or dips</span><span class="price">$3.00/person</span></div>
  <div class="price-row"><span>Stuffed Mushrooms</span><span class="price">$3.00/person</span></div>
  <div class="price-row"><span>Mini fried chicken and waffles<br>drizzled with maple syrup</span><span class="price">$4.00/person</span></div>
  <div class="price-row"><span>Shrimp cocktails with cocktail sauce</span><span class="price">$4.00/person</span></div>
</section>

<section class="section drinks">
  <h2 class="section-title">Drinks</h2>
  <p class="price-note">Includes cups &amp; ice</p>
  <div class="price-row"><span>12 oz. canned Soft Drinks</span><span class="price">$1.00 Ea</span></div>
  <div class="price-row"><span>16 oz. bottled water</span><span class="price">$1.00 Ea</span></div>
  <div class="price-row"><span>Gallon Tea (sweet or unsweetened)</span><span class="price">$6.00 Ea</span></div>
</section>

<div class="photo photo-pastries" role="img" aria-label="Tray of glazed cinnamon pinwheel pastries"></div>
<div class="photo photo-cupcakes" role="img" aria-label="Cupcakes with swirled chocolate frosting on a glass plate"></div>
<div class="photo photo-buffet" role="img" aria-label="Catered buffet table with red cloth and platters of food"></div>

</body>
</html>
```